Business Cards: Helena Marsh
Cards for an Artisan Jeweler
Business Cards: Helena Marsh -
Creative Brief
Cutting-Edge
Helena Marsh
Artisan Goldsmith
627 Wexley Road Suite 2-418 Florham Park, NJ 07519
hmarsh2014@examplemail.com
www.helenamarshstudio.com
Interested in creative, artistic design to business card that is reflective of upscale elegance with an edge. Please use colors in logo (black background and vertical orientation preferred). Open to text on front and back - designers preference.
Brunel Brunel
@project holder, Please see my last entry in large view. I need comments!
HelenaMarsh HelenaMarsh
Designers, I'm in love with these cards. I can't believe how hard it is to narrow down the selection. Just a brief note that my preference is to have rounded corners. I will likely ask for this in any final design selected. Thank you again.
Designers, thank you for your work thus far. I haven't been able to figure out how to respond back to your questions directly so I will try to write a few general comments. I do tend towards a darker colors and vertical cards. I don't like an overly busy card or straight edge graphics but I do like ornamentation. Also, I am open to alternative card sizes and shapes but am not sure if this site allows for that. More insights can be gleaned from my brief and once I can figure out how to respond directly, I will.

```html
<!DOCTYPE html>
<html lang="en">
<head>
<meta charset="utf-8">
<title>Helena Marsh — Business Cards</title>
<link href="https://fonts.googleapis.com/css2?family=Open+Sans:wght@400;600&display=swap" rel="stylesheet">
<style>
  :root {
    --backdrop: #5e4129;
    --card-white: #ffffff;
    --card-black: #1a1511;
    --gold: #a8862c;
    --gold-light: #d1b15a;
    --gold-deep: #7d6420;
    --ink: #2b2b2b;
    --web-light: #cfc6b4;
  }
  html, body {
    margin: 0;
    width: 1200px;
    height: 998px;
    overflow: hidden;
    background: var(--backdrop);
    font-family: "Open Sans", Arial, sans-serif;
  }
  .stage { position: relative; width: 1200px; height: 998px; }
  .card {
    position: absolute;
    width: 505px;
    height: 292px;
    overflow: hidden;
    box-shadow: 0 4px 14px rgba(0,0,0,.35);
  }
  .card--white { background: var(--card-white); }
  .card--black { background: var(--card-black); }
  .pos-tl { left: 89px; top: 108px; }
  .pos-tr { left: 606px; top: 108px; }
  .pos-bl { left: 89px; top: 432px; }
  .pos-br { left: 606px; top: 432px; }

  .contact { position: absolute; left: 22px; top: 26px; color: var(--ink); }
  .contact__name { margin: 0; font-size: 22px; font-weight: 600; color: var(--gold); line-height: 1.1; }
  .contact__role { margin: 2px 0 0; font-size: 12px; }
  .contact__address, .contact__lines { margin: 26px 0 0; font-size: 12px; line-height: 1.4; }
  .contact__lines { margin-top: 18px; }

  .ornament { position: absolute; top: 0; right: 0; bottom: 0; }
  .ornament--gold-field {
    width: 48%;
    background: linear-gradient(100deg, rgba(255,255,255,0) 0%, var(--gold-light) 30%, var(--gold) 70%, var(--gold-deep) 100%);
  }
  .ornament--dark-field {
    width: 44%;
    background: linear-gradient(100deg, rgba(26,21,17,0) 0%, var(--card-black) 26%, #2a2114 70%, var(--gold-deep) 100%);
  }

  .brand {
    position: absolute; left: 0; right: 0; top: 108px;
    text-align: center;
  }
  .brand__mark {
    display: inline-block; width: 14px; height: 14px;
    background: var(--gold); border-radius: 50%;
    vertical-align: middle; margin-right: 10px;
  }
  .brand__name {
    font-size: 30px; font-weight: 400; color: var(--gold);
    vertical-align: middle;
  }
  .web {
    position: absolute; left: 0; right: 0; bottom: 16px; margin: 0;
    text-align: center; font-size: 10px;
  }
  .card--black .web { color: var(--web-light); }
  .card--white .web { color: var(--ink); }
</style>
</head>
<body>
<main class="stage">

  <section class="card card--white pos-tl" aria-label="Business card front, white with gold field">
    <div class="ornament ornament--gold-field" role="img" aria-label="Black swirling flourish over gold panel"></div>
    <div class="contact">
      <h1 class="contact__name">Helena Marsh</h1>
      <p class="contact__role">Artisan Goldsmith</p>
      <p class="contact__address">627 Wexley Road<br>Suite 2-418<br>Alder Falls, OR 97519</p>
      <p class="contact__lines">Phone: 541.555.0148<br>Email: hmarsh2014@examplemail.com</p>
    </div>
  </section>

  <section class="card card--black pos-tr" aria-label="Business card back, black">
    <div class="brand"><span class="brand__mark"></span><span class="brand__name">Helena Marsh</span></div>
    <p class="web">www.helenamarshstudio.com</p>
  </section>

  <section class="card card--white pos-bl" aria-label="Business card back, white">
    <div class="brand"><span class="brand__mark"></span><span class="brand__name">Helena Marsh</span></div>
    <p class="web">www.helenamarshstudio.com</p>
  </section>

  <section class="card card--white pos-br" aria-label="Business card front, white with black field">
    <div class="ornament ornament--dark-field" role="img" aria-label="Gold swirling flourish over black panel"></div>
    <div class="contact">
      <h1 class="contact__name">Helena Marsh</h1>
      <p class="contact__role">Artisan Goldsmith</p>
      <p class="contact__address">627 Wexley Road<br>Suite 2-418<br>Alder Falls, OR 97519</p>
      <p class="contact__lines">Phone: 541.555.0148<br>Email: hmarsh2014@examplemail.com</p>
    </div>
  </section>

</main>
</body>
</html>
```